" KTR SOLUÇÕES EMPRESARIAIS atua desde abril de 2004 com o objetivo de contribuir com as Organizações na implantação e implementação de projetos específicos ou integrados de Gestão de Pessoas, Processos e Desenvolvimento Organizacional. Nossa equipe é formada por consultores multidisciplinares, experientes e comprometidos com o atendimento personalizado o que assegura a qualidade e eficácia dos serviços prestados. Nosso compromisso é criar uma forte parceria na busca de soluções de acordo com a cultura, valores, características, objetivos organizacionais, realidade e necessidades de cada empresa-cliente. "

```html
<!DOCTYPE html>
<html lang="pt-BR">
<head>
<meta charset="utf-8">
<title>KTR Soluções Empresariais – Cartão de visita</title>
<link rel="stylesheet" href="https://fonts.googleapis.com/css2?family=Jost:wght@400;500;600&display=swap">
<style>
  :root {
    --page-bg: #e9e6e1;
    --card-white: #ffffff;
    --gold: #b8924a;
    --navy: #1b2d58;
    --teal-blue: #1f5a7c;
    --text-light: #ffffff;
    --shadow: rgba(0, 0, 0, 0.18);
  }
  * { margin: 0; padding: 0; box-sizing: border-box; }
  html, body {
    width: 1200px;
    height: 1200px;
    overflow: hidden;
    background: var(--page-bg);
    font-family: "Jost", "Futura", sans-serif;
  }
  .canvas {
    position: relative;
    width: 1200px;
    height: 1200px;
  }
  .card {
    position: absolute;
    width: 761px;
    height: 418px;
    border-radius: 24px;
    box-shadow: 0 8px 24px var(--shadow);
    overflow: hidden;
  }
  .card--front {
    left: 163px;
    top: 132px;
    background: var(--card-white);
  }
  .card--back {
    left: 295px;
    top: 641px;
    background: linear-gradient(90deg, var(--teal-blue) 0%, var(--navy) 100%);
    color: var(--text-light);
  }
  .brand {
    position: absolute;
    display: flex;
    align-items: center;
    font-weight: 600;
    white-space: nowrap;
  }
  .brand__mark {
    display: block;
    flex: none;
  }
  .card--front .brand {
    left: 50%;
    top: 50%;
    transform: translate(-50%, -50%);
    gap: 22px;
    font-size: 58px;
    color: var(--gold);
  }
  .card--front .brand__mark {
    width: 58px;
    height: 58px;
    background: var(--gold);
  }
  .card--back .brand {
    left: 76px;
    top: 52px;
    gap: 14px;
    font-size: 34px;
    color: var(--text-light);
  }
  .card--back .brand__mark {
    width: 34px;
    height: 34px;
    background: var(--text-light);
  }
  .gold-rule {
    position: absolute;
    left: 46px;
    top: 43px;
    width: 5px;
    height: 347px;
    background: var(--gold);
  }
  .person-name {
    position: absolute;
    left: 76px;
    top: 190px;
    font-size: 36px;
    font-weight: 400;
    letter-spacing: 0.5px;
  }
  .contact {
    position: absolute;
    left: 76px;
    top: 286px;
    list-style: none;
    font-size: 19px;
    line-height: 36px;
    font-weight: 400;
  }
</style>
</head>
<body>
  <main class="canvas">
    <section class="card card--front" aria-label="Frente do cartão">
      <div class="brand">
        <span class="brand__mark"></span>
        <span class="brand__name">KTR Consultoria</span>
      </div>
    </section>

    <section class="card card--back" aria-label="Verso do cartão">
      <span class="gold-rule"></span>
      <div class="brand">
        <span class="brand__mark"></span>
        <span class="brand__name">KTR Consultoria</span>
      </div>
      <h1 class="person-name">Renato Albuquerque</h1>
      <ul class="contact">
        <li>Home Office - Vale Verde / RS</li>
        <li>+55 51 9034.2716 - renato@ktrconsultoria.com.br</li>
        <li>www.ktrconsultoria.com.br</li>
      </ul>
    </section>
  </main>
</body>
</html>
```